Vemarok Contracting Folder

Creating a design for the cover of our folders that we pass to our customers

Want to keep the same look as our colors and fonts as attached

```html
<!DOCTYPE html>
<html lang="en">
<head>
<meta charset="utf-8">
<title>Vemarok Contracting Folder</title>
<link href="https://fonts.googleapis.com/css2?family=Questrial&family=Arimo:wght@400;700&display=swap" rel="stylesheet">
<style>
  :root {
    --bg: #b7b7b7;
    --paper: #f7f7f8;
    --royal: #1b1fae;
    --royal-deep: #0d0f96;
    --royal-soft: #3a40c0;
    --sun: #f6cf33;
    --lavender: #a7aade;
    --ink: #13159f;
    --faint: rgba(150, 155, 230, 0.35);
    --pattern: #f1efe6;
  }
  * { box-sizing: border-box; margin: 0; padding: 0; }
  html, body { width: 842px; height: 1200px; overflow: hidden; background: var(--bg); }
  .canvas { position: relative; width: 842px; height: 1200px; }

  .spread { position: absolute; left: 41px; width: 760px; height: 507px; display: flex; box-shadow: 0 10px 24px rgba(0,0,0,0.25); }
  .spread--outer { top: 50px; }
  .spread--inner { top: 640px; }
  .panel { position: relative; width: 380px; height: 100%; overflow: hidden; }

  /* Back cover */
  .back-cover { background: linear-gradient(160deg, var(--royal-deep), var(--royal) 70%, var(--royal-soft)); }
  .back-cover__strip { position: absolute; left: 250px; top: 0; width: 62px; height: 100%; }
  .back-cover__cap { position: absolute; left: 0; top: 20px; width: 100%; height: 20px; background: var(--lavender); opacity: 0.8; }
  .back-cover__foot { position: absolute; left: 0; bottom: 70px; width: 100%; height: 38px; background: var(--sun); }
  .watermark-name, .watermark-sub {
    position: absolute; writing-mode: vertical-rl; white-space: nowrap;
    font-family: "Questrial", sans-serif; color: var(--faint); line-height: 1;
  }
  .watermark-name { left: 250px; top: 52px; font-size: 60px; letter-spacing: 1px; }
  .watermark-sub { left: 184px; top: 60px; font-size: 38px; letter-spacing: 8px; }
  .contact { position: absolute; left: 34px; bottom: 44px; font-family: "Arimo", sans-serif; font-style: normal; font-size: 7px; line-height: 1.35; color: #fff; }
  .contact__company { color: var(--sun); font-weight: 700; }
  .contact__line { display: flex; align-items: center; gap: 4px; }
  .contact__line svg { width: 7px; height: 7px; }
  .contact__address { margin-bottom: 4px; }

  /* Front cover */
  .front-cover { background: linear-gradient(200deg, #ffffff, var(--paper) 60%, #e9e9eb); }
  .masthead { position: absolute; top: 150px; left: 0; width: 100%; height: 70px; }
  .masthead__band-left { position: absolute; left: 0; top: 22px; width: 70px; height: 38px; background: var(--sun); }
  .masthead__band-right { position: absolute; right: 0; top: 0; width: 80px; height: 34px; background: var(--royal); }
  .wordmark { position: absolute; left: 86px; top: -4px; font-family: "Questrial", sans-serif; color: var(--ink); line-height: 1; }
  .wordmark__name { display: block; font-size: 42px; letter-spacing: 1px; }
  .wordmark__sub { display: block; font-size: 19px; letter-spacing: 3px; margin-top: 8px; padding-left: 10px; }
  .front-cover .wordmark__sub { color: var(--lavender); }

  /* Inner spread */
  .inner-panel { background: #f4f4f2; }
  .inner-panel__pattern { position: absolute; inset: 0; background: linear-gradient(180deg, #f6f5ef, var(--pattern)); }
  .pocket { position: absolute; left: 0; bottom: 0; width: 100%; height: 220px; box-shadow: 0 -4px 10px rgba(0,0,0,0.12); }
  .pocket--left { background: linear-gradient(170deg, var(--royal-deep), var(--royal) 60%, var(--royal-soft)); }
  .pocket--right { background: linear-gradient(190deg, var(--royal-deep), var(--royal) 55%, var(--royal-soft)); }
  .card-slits { position: absolute; left: 120px; top: 50px; width: 120px; height: 90px; }
  .pocket__band-left { position: absolute; left: 0; top: 48px; width: 150px; height: 30px; background: var(--sun); }
  .pocket__band-right { position: absolute; right: 0; top: 82px; width: 90px; height: 22px; background: var(--lavender); }
  .pocket__wordmark { position: absolute; left: 160px; top: 44px; font-family: "Questrial", sans-serif; color: #fff; line-height: 1; }
  .pocket__wordmark .wordmark__name { font-size: 30px; }
  .pocket__wordmark .wordmark__sub { font-size: 12px; letter-spacing: 2px; margin-top: 5px; padding-left: 6px; }
</style>
</head>
<body>
<main class="canvas">

  <section class="spread spread--outer" aria-label="Folder outside">
    <div class="panel back-cover">
      <div class="back-cover__strip">
        <div class="back-cover__cap"></div>
        <div class="back-cover__foot"></div>
      </div>
      <span class="watermark-name" aria-hidden="true">VEMAROK</span>
      <span class="watermark-sub" aria-hidden="true">Contracting</span>
      <address class="contact">
        <div class="contact__company">Vemarok Contracting Ltd</div>
        <div class="contact__address">214 Alderbrook Lane<br>Kenwick, Alaska 34590</div>
        <div class="contact__line"><svg viewBox="0 0 10 10"><path d="M2 1l2 2-1 1.5a6 6 0 0 0 2.5 2.5L7 6l2 2-1.5 1.5C4 9 1 6 .5 2.5z" fill="#fff"/></svg>555 214 0187</div>
        <div class="contact__line"><svg viewBox="0 0 10 10"><rect x="2" y="1" width="6" height="8" fill="none" stroke="#fff"/></svg>555 326 4410</div>
        <div class="contact__line"><svg viewBox="0 0 10 10"><rect x="1" y="3" width="8" height="5" fill="#fff"/></svg>555 781 9023</div>
        <div class="contact__line"><svg viewBox="0 0 10 10"><rect x="1" y="2" width="8" height="6" fill="none" stroke="#fff"/><path d="M1 2l4 3 4-3" fill="none" stroke="#fff"/></svg>info@vemarokcontracting.com</div>
        <div class="contact__line"><svg viewBox="0 0 10 10"><circle cx="5" cy="5" r="4" fill="#fff"/></svg>www.vemarokcontracting.com</div>
      </address>
    </div>
    <div class="panel front-cover">
      <div class="masthead">
        <div class="masthead__band-left"></div>
        <div class="wordmark">
          <span class="wordmark__name">VEMAROK</span>
          <span class="wordmark__sub">Contracting</span>
        </div>
        <div class="masthead__band-right"></div>
      </div>
    </div>
  </section>

  <section class="spread spread--inner" aria-label="Folder inside">
    <div class="panel inner-panel">
      <div class="inner-panel__pattern" role="img" aria-label="Faint yellow and grey striped background pattern"></div>
      <div class="pocket pocket--left">
        <svg class="card-slits" viewBox="0 0 120 90" aria-hidden="true">
          <path d="M10 10h14M100 30v12M70 80h14" stroke="#fff" stroke-width="1.5"/>
        </svg>
      </div>
    </div>
    <div class="panel inner-panel">
      <div class="inner-panel__pattern" role="img" aria-label="Faint yellow and grey striped background pattern"></div>
      <div class="pocket pocket--right">
        <div class="pocket__band-left"></div>
        <div class="pocket__wordmark">
          <span class="wordmark__name">VEMAROK</span>
          <span class="wordmark__sub">Contracting</span>
        </div>
        <div class="pocket__band-right"></div>
      </div>
    </div>
  </section>

</main>
</body>
</html>
```